Card design for Heating and Cooling company

this is for a heating and cooling company we recently updated our logo and need to update our cards. We attached our logo so you can incorporate it into the card. We specialize in residential and commercial furnace and air condition repairs. Have been in business since 2014.

Phone number 555.284.9137

We need the following phrases
:Repairs, Installations, and maintenance
:Quality work at reasonable prices
:residential/commercial
:Licensed &Insured
:Email Pinegrovehvac47@mailbox-example.com
Name: Teodor K (Ted)
Also on back side I would like my logo with wording :Thank you for your business and refferal

Industry/Entity Type

Hvac

Contact Information for Business Card

:residential/commercial
:Licensed & Insured
Name: Teodor K (Ted)
Number:555.284.9136

Requirements
Must have
• Blue and red colors
Nice to have
• Maybe a pic of a furnace or air conditioner

```html
<!DOCTYPE html>
<html lang="en">
<head>
<meta charset="utf-8">
<title>Pinegrove Heating &amp; Cooling — Business Card</title>
<link href="https://fonts.googleapis.com/css2?family=Source+Sans+3:wght@400;600;700;800&display=swap" rel="stylesheet">
<style>
  :root {
    --backdrop: #6e7785;
    --paper: #ffffff;
    --ink: #111111;
    --night: #000000;
    --frost-blue: #12a6ea;
    --flame-red: #ff3a1c;
    --on-band: #ffffff;
  }
  * { box-sizing: border-box; margin: 0; padding: 0; }
  html, body { width: 1200px; height: 739px; overflow: hidden; }
  body {
    position: relative;
    background: var(--backdrop);
    font-family: "Source Sans 3", sans-serif;
  }
  .card {
    position: absolute;
    left: 345px;
    width: 502px;
    height: 301px;
    overflow: hidden;
  }
  .card--front { top: 61px; background: var(--paper); }
  .card--back { top: 378px; background: var(--night); }

  .brand-name {
    position: absolute;
    text-align: center;
    font-family: "Source Sans 3", sans-serif;
    font-weight: 800;
    text-transform: uppercase;
    line-height: 1;
  }
  .brand-name .brand-line { display: block; font-size: 28px; letter-spacing: 0.5px; }
  .brand-name .brand-sub { display: block; font-size: 7px; letter-spacing: 5px; margin-top: 3px; }
  .card--front .brand-name { left: 35px; top: 136px; width: 160px; color: var(--ink); }
  .card--back .brand-name { left: 170px; top: 133px; width: 160px; color: var(--paper); }

  .divider {
    position: absolute;
    left: 212px;
    top: 119px;
    width: 1px;
    height: 58px;
    background: var(--frost-blue);
  }
  .contact {
    position: absolute;
    left: 230px;
    right: 28px;
    top: 116px;
    color: var(--ink);
  }
  .contact-name {
    font-size: 18px;
    font-weight: 700;
    color: var(--frost-blue);
    line-height: 22px;
    margin-bottom: 5px;
  }
  .contact-line { font-size: 13.5px; line-height: 20px; white-space: nowrap; }

  .band {
    position: absolute;
    left: 0;
    width: 100%;
    height: 19px;
    text-align: center;
    color: var(--on-band);
    font-size: 14.5px;
    line-height: 19px;
  }
  .band--services { top: 238px; background: var(--frost-blue); }
  .band--promise { top: 262px; background: var(--flame-red); }

  .thanks {
    position: absolute;
    left: 0;
    width: 100%;
    top: 261px;
    text-align: center;
    color: var(--paper);
    font-size: 14.5px;
    line-height: 20px;
  }
</style>
</head>
<body>
  <section class="card card--front" aria-label="Card front">
    <div class="brand-name">
      <span class="brand-line">Pinegrove</span>
      <span class="brand-sub">Heating &amp; Cooling</span>
    </div>
    <div class="divider"></div>
    <div class="contact">
      <p class="contact-name">Teodor K (Ted)</p>
      <p class="contact-line">555.284.9136</p>
      <p class="contact-line">Pinegrovehvac47@mailbox-example.com</p>
    </div>
    <p class="band band--services">Quality Work at Reasonable Prices - Residential/Commercial</p>
    <p class="band band--promise">Repairs, Installations, and Maintenance - Licensed &amp; Insured</p>
  </section>

  <section class="card card--back" aria-label="Card back">
    <div class="brand-name">
      <span class="brand-line">Pinegrove</span>
      <span class="brand-sub">Heating &amp; Cooling</span>
    </div>
    <p class="thanks">Thank you for your business and refferal</p>
  </section>
</body>
</html>
```